New Banner Ad Design Project

We are a start-up in San Francisco that sells consignment clothes with a percentage of the proceeds donated to charity. Also, volunteer groups can conduct dress drives and send them to us and we will sell them and give their charity back 60% of the proceeds.

We have several uses for banners:
- Home page banner:
- Promote timely Flash Sales (they last only 96 hours) which happen 2x/week
- Promote how good it feels to give back and shop
- Promote any special promotions such as a Gift With Purchase
- Community banner:
- Promote the lifestyle
- Promote any particular group conducting a dress drive

If you are going to submit one banner it is to be for an upcoming sale, as the two attached files address (maternity sale). If we find the right designer we will consider working with them beyond the design contest for future sale banners as well as others

We consider our 'competitors' to be The Garment Harbor, The TrueLoop, WovaSpin, KnitPeak, GlowAgain. Our key differentiator is the charitable components and how groups are conducting dress drives to raise money.

We are in the midst of changing our company name, tagline and logo. The new company will be called 'TessaLume' and our tagline is 'Restitched Kindness'

Target Market(s)

Our initial audience is young women 16 - 30. We will be focusing on Prom February through May which appeals to 16 - 18 year olds.

We also have maternity-wear. We want these women to feel fashionable

We are focused on individuals who want to give back.

Industry/Entity Type

Charity

Font styles to use
Serif
Sans Serif

Colors
8769ae
1b1b1b
474747
c3c3c3
86cfc6
b7a5cd

Requirements
Must have
• - Youthful and stylish voice (not to be confused with Young)
- Appealing visuals
- Powerful call-to-action as it pertains to banners for our flash sales
- An inclusive feel
- Communicates our charitable component
Nice to have
• - Emotional appeal
- Women wearing our clothes (see attached)
Should not have
• - Too much text
- Too girly; overly flowery

```html
<!DOCTYPE html>
<html lang="en">
<head>
<meta charset="utf-8">
<title>Maternity Sale Banner</title>
<link rel="stylesheet" href="https://fonts.googleapis.com/css2?family=Raleway:wght@300;400;800&display=swap">
<style>
  :root {
    --panel-grey: #959595;
    --divider-white: #ffffff;
    --type-white: #ffffff;
    --button-purple: #563f7e;
    --photo-light: #f4ece4;
    --photo-mid: #e3c9b2;
    --photo-shadow: #6b5a55;
    --photo-dark: #2a2a30;
  }
  html, body {
    margin: 0;
    padding: 0;
    width: 1200px;
    height: 553px;
    overflow: hidden;
    background: var(--divider-white);
  }
  .sale-banner {
    display: block;
    width: 1200px;
    height: 553px;
    font-family: "Raleway", sans-serif;
  }
  .headline-maternity { font-weight: 300; fill: var(--type-white); font-size: 104px; }
  .headline-sale { font-weight: 800; fill: var(--type-white); font-size: 222px; }
  .charity-line { font-weight: 300; fill: var(--type-white); font-size: 43px; }
  .cta-label { font-weight: 400; fill: var(--type-white); font-size: 25px; }
  .panel { fill: var(--panel-grey); }
  .cta-button { fill: var(--button-purple); }
  .photo-divider { stroke: var(--divider-white); stroke-width: 10; }
  .bag-icon { fill: var(--type-white); }
  .bag-handle { fill: none; stroke: var(--type-white); stroke-width: 2; }
  .photo-tone-light { stop-color: var(--photo-light); }
  .photo-tone-mid { stop-color: var(--photo-mid); }
  .photo-tone-shadow { stop-color: var(--photo-shadow); }
  .photo-tone-dark { stop-color: var(--photo-dark); }
</style>
</head>
<body>
<svg class="sale-banner" viewBox="0 0 1200 553" xmlns="http://www.w3.org/2000/svg">
  <defs>
    <linearGradient id="photoTone" x1="0" y1="0" x2="1" y2="1">
      <stop offset="0" class="photo-tone-light"/>
      <stop offset="0.45" class="photo-tone-mid"/>
      <stop offset="0.8" class="photo-tone-shadow"/>
      <stop offset="1" class="photo-tone-dark"/>
    </linearGradient>
  </defs>

  <polygon class="model-photo" points="839,0 1200,0 1200,553 659,553" fill="url(#photoTone)"
           role="img" aria-label="Photo of a woman in sunglasses and a dark beaded jacket"/>
  <line class="photo-divider" x1="751" y1="264" x2="1200" y2="0"/>
  <line class="photo-divider" x1="747" y1="281" x2="1200" y2="527"/>

  <polygon class="panel" points="0,0 817,0 645,553 0,553"/>

  <text class="headline-maternity" x="58" y="92" textLength="607" lengthAdjust="spacingAndGlyphs">MATERNITY</text>
  <text class="headline-sale" x="53" y="264" textLength="612" lengthAdjust="spacingAndGlyphs">SALE</text>
  <text class="charity-line" x="56" y="332" textLength="609" lengthAdjust="spacingAndGlyphs">60% IS DONATED TO CHARITY</text>

  <g class="shop-now-button">
    <circle class="cta-button" cx="338" cy="452" r="82"/>
    <text class="cta-label" x="336" y="450" text-anchor="middle">SHOP NOW</text>
    <path class="bag-handle" d="M331 468 q0 -9 6 -9 q6 0 6 9"/>
    <polygon class="bag-icon" points="323,466 351,466 353,502 320,502"/>
  </g>
</svg>
</body>
</html>
```